Banner poster with different motifs

I'm looking for 5 banners and posters in A1 format in the same design, or the similarity must be recognizable...
Kept quite simple with different titles.

1 ballet
2 Contemporary Dance
3 high heels
4 Salsa & Bachata & Zouk
5 Hip Hop

Modern bright colors
it is for the entrance so that the students see here is a dance school

The text may also be included in the image
The photos are for guidance only; some are our own, some are purchased. However, we are permitted to use them, including our logo, of course.

```html
<!DOCTYPE html>
<html lang="en">
<head>
<meta charset="utf-8">
<title>Velora Dance Center – High Heels</title>
<link rel="stylesheet" href="https://fonts.googleapis.com/css2?family=Roboto:wght@300;400;700&display=swap">
<style>
  :root {
    --pink: #ff61c6;
    --sun: #fdbb5a;
    --white: #ffffff;
    --shadow: #8b2d6e;
    --photo-dark: #1a1a1a;
    --photo-mid: #3a3034;
    --title-shadow: rgba(120, 20, 90, 0.35);
  }
  * { margin: 0; padding: 0; box-sizing: border-box; }
  html, body {
    width: 1200px;
    height: 847px;
    overflow: hidden;
    background: var(--pink);
  }
  .poster {
    position: relative;
    width: 1200px;
    height: 847px;
    background: var(--pink);
    font-family: "Roboto", Arial, sans-serif;
    color: var(--white);
    overflow: hidden;
  }
  .artwork {
    position: absolute;
    inset: 0;
  }
  .brand {
    position: absolute;
    top: 27px;
    left: 0;
    width: 1200px;
    text-align: center;
    font-weight: 300;
    color: var(--white);
  }
  .brand-mark {
    display: block;
    width: 60px;
    height: 60px;
    margin: 0 auto 6px;
    border: 1.5px solid var(--white);
    border-radius: 50%;
  }
  .brand-name {
    font-size: 26px;
    letter-spacing: 2px;
    line-height: 1;
  }
  .brand-tagline {
    margin-top: 5px;
    font-size: 8px;
    letter-spacing: 2.6px;
    line-height: 1;
  }
  .headline {
    position: absolute;
    left: 600px;
    top: 172px;
    font-weight: 400;
    font-size: 161px;
    line-height: 142px;
    letter-spacing: -2px;
    text-shadow: 6px 8px 10px var(--title-shadow);
  }
  .class-list {
    position: absolute;
    left: 609px;
    top: 478px;
    font-weight: 700;
    font-size: 16.5px;
    line-height: 26px;
    letter-spacing: 0.3px;
  }
  .footer-line {
    position: absolute;
    left: 0;
    top: 745px;
    width: 1200px;
    text-align: center;
    font-weight: 400;
    font-size: 15px;
    letter-spacing: 10.5px;
    word-spacing: 14px;
  }
</style>
</head>
<body>
  <main class="poster">
    <svg class="artwork" width="1200" height="847" viewBox="0 0 1200 847">
      <defs>
        <linearGradient id="dancer-tones" x1="0" y1="0" x2="1" y2="1">
          <stop offset="0" stop-color="var(--photo-mid)"/>
          <stop offset="1" stop-color="var(--photo-dark)"/>
        </linearGradient>
      </defs>
      <circle class="dot dot-top" cx="192" cy="150" r="43" fill="var(--sun)"/>
      <circle class="sun-disc" cx="356" cy="384" r="223" fill="var(--sun)"/>
      <circle class="dot dot-low-left" cx="187" cy="621" r="29" fill="var(--sun)"/>
      <circle class="dot dot-low-right" cx="580" cy="659" r="49" fill="var(--sun)"/>
      <ellipse class="floor-shadow" cx="355" cy="709" rx="200" ry="14" fill="var(--shadow)"/>
      <rect class="dancer-photo" role="img"
            aria-label="Photo of a dancer kneeling in a black bodysuit, long black patent gloves and thigh-high heeled boots"
            x="196" y="216" width="396" height="496" rx="28"
            fill="url(#dancer-tones)"/>
    </svg>

    <header class="brand">
      <span class="brand-mark"></span>
      <div class="brand-name">VELORA</div>
      <div class="brand-tagline">DANCE CENTER FRANKFURT</div>
    </header>

    <h1 class="headline">HIGH<br>HEELS</h1>

    <p class="class-list">
      BALLET &nbsp;/&nbsp; CONTEMPORARY DANCE &nbsp;/&nbsp; HIGH HEELS<br>
      SALSA &amp; BACHATA &amp; ZOUK &nbsp;/&nbsp; HIP HOP
    </p>

    <p class="footer-line">VELORA DANCE CENTER FRANKFURT</p>
  </main>
</body>
</html>
```